Marrow Aviation Group - "Coming Soon" Main Company Webpage

Design a main webpage that can be posted while a fully functional website is constructed. The design should be created to convey a sense of luxury and exclusivity. The main page should contain only one photo as the background. The photo I believe to show "luxury" and "Exclusivity" is listed as "Global Luxury Photo". I have included two other photos as well to aid in providing a variety of presentations.
The "Member TFPS" logo should appear somewhere on the main page but be less prevalent than the main company logo. "Coming Soon" should also appear to convey that a website is being constructed.
Tabs for the website:
- Aircraft Management
- Aircraft Sales
- Pilot Services
- Charter
- Flight Training

```html
<!DOCTYPE html>
<html lang="en">
<head>
<meta charset="utf-8">
<title>Marrow Aviation Group – Coming Soon</title>
<link rel="stylesheet" href="https://fonts.googleapis.com/css2?family=Bodoni+Moda:opsz,wght@6..96,400;6..96,500;6..96,700;6..96,800&family=Montserrat:wght@500&display=swap">
<style>
  :root {
    --brand-blue: #1461ad;
    --ink: #111111;
    --nav-ink: #2a2a2a;
    --paper: #ffffff;
    --footer-bg: #000000;
    --footer-ink: #ffffff;
    --sky-top: #3f6e9c;
    --sky-mid: #9fbbd9;
    --sky-glow: #e9c9d3;
    --cloud: #d9d3e2;
  }
  * { box-sizing: border-box; margin: 0; padding: 0; }
  html, body {
    width: 1200px;
    height: 671px;
    overflow: hidden;
    background: var(--paper);
  }
  .page {
    position: relative;
    width: 1200px;
    height: 671px;
    font-family: "Bodoni Moda", "Didot", serif;
  }
  .site-header {
    position: absolute;
    top: 0; left: 0;
    width: 1200px;
    height: 111px;
    background: var(--paper);
  }
  .brand {
    position: absolute;
    left: 110px;
    top: 26px;
    color: var(--brand-blue);
    font-weight: 800;
    font-size: 27px;
    line-height: 29px;
    letter-spacing: 0.5px;
  }
  .main-nav {
    position: absolute;
    left: 388px;
    top: 38px;
    display: flex;
    gap: 24px;
  }
  .main-nav a {
    color: var(--nav-ink);
    text-decoration: none;
    font-size: 19px;
    font-weight: 500;
    white-space: nowrap;
  }
  .hero {
    position: absolute;
    top: 111px; left: 0;
    width: 1200px;
    height: 515px;
  }
  .hero-photo {
    position: absolute;
    inset: 0;
    background:
      radial-gradient(ellipse 70% 40% at 75% 80%, rgba(240,196,206,0.85), rgba(240,196,206,0) 70%),
      linear-gradient(180deg, var(--sky-top) 0%, var(--sky-mid) 35%, var(--sky-glow) 72%, var(--cloud) 100%);
  }
  .announcement {
    position: absolute;
    left: 716px;
    top: 140px;
    width: 401px;
    text-align: center;
  }
  .coming-soon {
    color: var(--ink);
    font-size: 54px;
    font-weight: 700;
    letter-spacing: -1px;
    line-height: 1;
    white-space: nowrap;
  }
  .membership {
    position: relative;
    margin: 14px auto 0;
    width: 200px;
    height: 50px;
  }
  .membership-label {
    position: absolute;
    left: 63px;
    top: 0;
    font-family: "Montserrat", Arial, sans-serif;
    font-size: 12px;
    font-weight: 500;
    color: var(--ink);
  }
  .membership-mark {
    position: absolute;
    left: 0;
    top: 16px;
    width: 50px;
    height: 34px;
  }
  .membership-name {
    position: absolute;
    left: 63px;
    top: 15px;
    font-size: 30px;
    font-weight: 700;
    color: var(--ink);
    letter-spacing: 3px;
    line-height: 1;
  }
  .site-footer {
    position: absolute;
    left: 0;
    top: 626px;
    width: 1200px;
    height: 45px;
    background: var(--footer-bg);
    display: flex;
    align-items: center;
    justify-content: center;
  }
  .site-footer p {
    color: var(--footer-ink);
    font-size: 16px;
    font-weight: 700;
  }
</style>
</head>
<body>
<div class="page">
  <header class="site-header">
    <div class="brand">Marrow<br>Aviation Group</div>
    <nav class="main-nav">
      <a href="#">Aircraft Management</a>
      <a href="#">Aircraft Sales</a>
      <a href="#">Pilot Services</a>
      <a href="#">Charter</a>
      <a href="#">Flight Training</a>
    </nav>
  </header>

  <section class="hero">
    <div class="hero-photo" role="img" aria-label="Photograph of a white passenger jet flying above a sea of clouds at sunset under a blue and pink sky"></div>
    <div class="announcement">
      <h1 class="coming-soon">COMING SOON...</h1>
      <div class="membership">
        <span class="membership-label">member of</span>
        <svg class="membership-mark" viewBox="0 0 50 34" aria-hidden="true">
          <circle cx="25" cy="17" r="17" fill="var(--brand-blue)"/>
        </svg>
        <span class="membership-name">TFPS</span>
      </div>
    </div>
  </section>

  <footer class="site-footer">
    <p>Copyrights 2023 Marrow Aviation Group. All Rights Reserved.</p>
  </footer>
</div>
</body>
</html>
```